TIDE CREST MARINE Business card

Card for boat detailing business in Bermuda

Target Market(s)

clients. new clients

Industry/Entity Type

Marine

Contact Information for Business Card

TIDE CREST MARINE
Boat Maintenance & Detailing
Dorian K. Whitfield
P: 441 672 4159
E: dwhitfield@tidecrest.example
P.O. Box HL518
Hollow HLBX
Bermuda

Font styles to use
Sans Serif

Colors
85acd3
eaf1f7
0455a3
33b8a4
86cfc6
ffffff
cfdeed

Requirements
Must have
• ALL the information provided. Tropical, water, sky, blue/green/white elements.
Nice to have
• A silhoette of the boat in the photos provided.
Should not have
• Keep it simple and clean. Nothing over the top.

```html
<!DOCTYPE html>
<html lang="en">
<head>
<meta charset="utf-8">
<title>Tide Crest Marine – Business Card</title>
<link rel="stylesheet" href="https://fonts.googleapis.com/css2?family=Fira+Sans+Extra+Condensed:wght@600&family=Lato:wght@400&display=swap">
<style>
  :root {
    --backdrop: #2b2b2b;
    --paper: #ffffff;
    --teal-deep: #0c8b7d;
    --teal-title: #0e8a7b;
    --aqua: #4cf3fc;
    --aqua-dark: #22c3cf;
    --ink: #4a4a4a;
    --white: #ffffff;
  }
  * { margin: 0; padding: 0; box-sizing: border-box; }
  html, body {
    width: 1200px; height: 1200px; overflow: hidden;
    background: var(--backdrop);
  }
  .canvas { position: relative; width: 1200px; height: 1200px; }
  .card {
    position: absolute; top: 310px;
    width: 364px; height: 594px; overflow: hidden;
  }
  .card svg.waves { position: absolute; inset: 0; }
  .card-front { left: 234px; background: var(--paper); }
  .card-back { left: 627px; width: 369px; background: var(--teal-deep); }

  .brand {
    position: absolute; left: 0; right: 0;
    font-family: "Fira Sans Extra Condensed", "Arial Narrow", sans-serif;
    font-weight: 600; font-size: 52px; line-height: 61px;
    text-align: center; letter-spacing: 0.5px;
  }
  .card-front .brand { top: 88px; color: var(--teal-title); }
  .card-back .brand { top: 199px; color: var(--aqua-dark); }

  .person, .tagline, .contact, .address {
    position: absolute; font-family: "Lato", Arial, sans-serif; font-weight: 400;
  }
  .person {
    top: 256px; left: 0; right: 0; text-align: center;
    font-size: 21px; color: var(--ink);
  }
  .contact {
    left: 30px; top: 497px; list-style: none;
    font-size: 20px; line-height: 27px; color: var(--white);
  }
  .contact li { display: flex; align-items: center; gap: 8px; }
  .contact svg { width: 18px; height: 16px; fill: var(--white); }
  .tagline {
    top: 336px; left: 0; right: 0; text-align: center;
    font-size: 17.5px; color: var(--white);
  }
  .address {
    top: 507px; left: 10px; right: 0; text-align: center;
    font-size: 17px; line-height: 22px; color: var(--white);
  }
</style>
</head>
<body>
<main class="canvas">
  <section class="card card-front" aria-label="Business card front">
    <svg class="waves" viewBox="0 0 364 594" width="364" height="594" aria-hidden="true">
      <path fill="var(--aqua)" d="M0,244 C60,390 190,488 364,532 L364,594 L0,594 Z"/>
      <path fill="var(--aqua-dark)" d="M4,236 C70,370 200,465 364,502 L364,517 C200,482 75,385 4,236 Z"/>
    </svg>
    <h1 class="brand">TIDE CREST<br>MARINE</h1>
    <p class="person">DORIAN K. WHITFIELD</p>
    <ul class="contact">
      <li><svg viewBox="0 0 18 16"><path d="M2,5 C2,2 16,2 16,5 L13,7 L12,5 C10,4 8,4 6,5 L5,7 Z M4,9 L6,6 L12,6 L14,9 L14,13 L4,13 Z"/></svg>441 672 4159</li>
      <li><svg viewBox="0 0 18 16"><path d="M1,3 L17,3 L9,9 Z M1,4.5 L9,10.5 L17,4.5 L17,13 L1,13 Z"/></svg>dwhitfield@tidecrest.example</li>
    </ul>
  </section>

  <section class="card card-back" aria-label="Business card back">
    <svg class="waves" viewBox="0 0 369 594" width="369" height="594" aria-hidden="true">
      <path fill="var(--aqua)" d="M193,0 L369,0 L369,162 C310,95 255,40 193,0 Z"/>
      <path fill="var(--aqua-dark)" d="M200,0 C265,45 320,100 369,160 L369,150 C325,95 275,45 222,0 Z"/>
      <path fill="var(--aqua)" d="M0,432 C40,495 85,550 135,594 L0,594 Z"/>
      <path fill="var(--aqua-dark)" d="M20,448 C60,510 110,560 165,594 L140,594 C95,558 55,515 20,448 Z"/>
    </svg>
    <h2 class="brand">TIDE CREST<br>MARINE</h2>
    <p class="tagline">BOAT MAINTENANCE &amp; DETAILING</p>
    <p class="address">P.O. Box HL518 Hollow<br>HLBX Bermuda</p>
  </section>
</main>
</body>
</html>
```